Refresh look of our invoices (Excel spreadsheet which converts to PDF) to better match our new look

We have recently updated our Website and other marketing material with a new look and would like to refresh our invoice template so that it better matches our new look.  The template is an excel spreadsheet which we convert to a PDF to send out to our clients.
The main requirement is to incorporate the newer design colours and general look/feel to align with what is on our website www.corvalhill.com.au
It is extremely important that excel formula functionality and general layout are much the same although we are open to any design suggestions you might have.
Please note:
-Totals figures and news panel must remain on the first page
-We need full ability to edit embedded formulas and Excel spreadsheet is NOT to be password protected as we will only be using it internally.
-It is crucial that the second and subsequent pages can be extended (duplicated) internally to allow for larger multi page entries. Some of our clients invoices run up to 4/5 pages in length and we need the abilty to keep adding rows)
-possibility to add a "convert to PDF" button within the sheet which provides a 1 click solution to convert to PDF rather than the manual 2 step process to convert.... If that can be done, we would not want the "convert to PDF" button to show on final PDF converted version we issue to our customers.   Ideally, a single "convert to PDF and print first cover page only" in 1 single click button named 'convert to PDF & print' would be really handy.  -  (Just to explain why - we email out a PDF version of invoice to our clients and only print off first page with totals for our records)
The design for the first page can be different from the second & subsequent pages (eg first page can be more fancy with following pages more basic)

Finance Industry
Marketing

```html
<!DOCTYPE html>
<html lang="en">
<head>
<meta charset="utf-8">
<title>Corval Hill – Recipient Created Tax Invoice</title>
<link href="https://fonts.googleapis.com/css2?family=Arimo:wght@400;700&family=Montserrat:wght@600&display=swap" rel="stylesheet">
<style>
:root{
  --canvas:#dcdcdc;
  --paper:#ffffff;
  --ink:#333333;
  --ink-dark:#222222;
  --rule:#3d3d3d;
  --green:#7cb82f;
  --red:#e02020;
  --band:#3e3e3e;
}
*{box-sizing:border-box;margin:0;padding:0}
html,body{width:961px;height:1200px;overflow:hidden}
body{background:var(--canvas);font-family:"Arimo",Arial,sans-serif;color:var(--ink);position:relative}
.page{position:absolute;left:20px;width:921px;background:var(--paper);box-shadow:0 2px 6px rgba(0,0,0,.25)}
.page--cover{top:16px;height:580px}
.page--detail{top:606px;height:578px}
.abs{position:absolute}

/* cover */
.brand{left:62px;top:52px;display:flex;align-items:center;gap:12px}
.brand-mark{width:30px;height:30px;background:var(--rule)}
.brand-name{font-family:"Montserrat",Arial,sans-serif;font-weight:600;font-size:40px;letter-spacing:2px;color:var(--rule)}
.site{right:112px;top:80px;font-size:11px;font-weight:700;color:var(--green)}
.head-rule{left:62px;right:112px;top:108px;border-top:4px solid var(--rule)}
.abn{right:112px;top:120px;font-size:10px;font-weight:700;color:var(--ink)}
.doc-title{left:0;right:0;top:134px;text-align:center;font-size:15px;font-weight:700;color:var(--ink-dark)}
.inv-date{right:170px;top:156px;font-size:10.5px;font-weight:700}
.referrer{left:62px;top:176px;font-size:10px;font-weight:700;line-height:18px}
.referrer .gap{margin-top:14px}
.totals{right:112px;top:258px;width:300px;font-size:12px;font-weight:700;color:var(--ink-dark)}
.totals .row{display:flex;justify-content:space-between;height:16px}
.totals .row span:first-child{flex:1;text-align:right;padding-right:36px}
.totals .row span:last-child{width:90px;text-align:right;padding-right:6px}
.neg{color:var(--red)}
.totals .grand{margin-top:2px}
.totals .grand span:last-child{border:2px solid var(--ink-dark);height:18px;line-height:14px}
.info{left:62px;right:112px;top:426px}
.news{font-size:9.6px;font-weight:700;line-height:12.5px;color:var(--ink-dark)}
.news-title{color:var(--red)}
.news a{color:var(--green);text-decoration:none}
.privacy{margin-top:3px;border:1.5px solid var(--ink-dark);font-size:8px;font-style:italic;line-height:10.5px;padding:2px 4px}
.footer{margin-top:10px;font-size:9.6px;font-weight:700;color:var(--ink-dark)}

/* detail */
.detail-ref{left:62px;top:70px;font-size:10px;font-weight:700}
.ledger{left:52px;top:110px;width:743px;border-collapse:collapse;font-size:10.5px}
.ledger th{background:var(--band);color:var(--green);font-weight:700;height:26px;font-size:10.5px}
.ledger td{text-align:center;height:12.6px;line-height:12.6px;color:var(--ink-dark)}
.ledger col.c1{width:100px}.ledger col.c2{width:98px}.ledger col.c3{width:110px}.ledger col.c4{width:86px}
.ledger col.c5{width:86px}.ledger col.c6{width:66px}.ledger col.c7{width:74px}.ledger col.c8{width:123px}
.rule-notes{left:52px;top:342px;width:743px;font-size:10.5px;line-height:13px}
.rule-notes .row{display:flex}
.rule-notes .label{width:394px;color:var(--red)}
.rule-notes .label u{text-decoration:underline}
.rule-notes .v{text-align:center}
.summary{left:52px;top:372px;width:743px;border-collapse:collapse}
.summary th{background:var(--band);color:var(--green);font-size:10.5px;height:15px}
.summary td{text-align:center;font-weight:700;font-size:12px;height:30px;color:var(--ink-dark)}
.summary td.neg{color:var(--red)}
.summary td.boxed span{display:inline-block;border:2px solid var(--ink-dark);padding:2px 14px}
</style>
</head>
<body>

<section class="page page--cover">
  <div class="abs brand"><span class="brand-mark"></span><span class="brand-name">CORVAL HILL</span></div>
  <div class="abs site">www.corvalhill.com.au</div>
  <div class="abs head-rule"></div>
  <div class="abs abn">ABN&nbsp; 00 111 222 333</div>
  <h1 class="abs doc-title">RECIPIENT CREATED TAX INVOICE</h1>
  <div class="abs inv-date">Invoice Date:&nbsp; 13-Sep-13</div>
  <div class="abs referrer">
    <div>Referrer name</div>
    <div>referrer address line 1</div>
    <div>referrer address line 2</div>
    <div class="gap">ABN: 00 000 000 000</div>
  </div>
  <div class="abs totals">
    <div class="row"><span>Upfront</span><span>$3,000.00</span></div>
    <div class="row"><span>Trail</span><span>$202.26</span></div>
    <div class="row"><span>Adjustments</span><span class="neg">-$50.00</span></div>
    <div class="row"><span>GST</span><span>$315.24</span></div>
    <div class="row grand"><span>TOTAL AMOUNT DEPOSITED</span><span>$3,467.50</span></div>
  </div>
  <div class="abs info">
    <div class="news">
      <div class="news-title">* CORVAL CONNECT - Referral management software *</div>
      The Corval Connect software provides you with a fully compliant referral process that is supported by the lenders. Apart from making new referrals, you can also read lender updates on deal progress and lodge enquires for outstanding commission payments. You can login by going to the dedicated Corval Connect website at: <a>www.corvalmembers.com.au</a>
    </div>
    <div class="privacy">This report contains confidential client information. Disclosure of customer information such as loan details and lenders to third parties may be a contravention of the Privacy Act, unless they are authorised to receive such details.</div>
    <div class="footer">Corval Hill Pty Ltd&nbsp; Level 12, 88 Harbour Lane Melbourne Vic 3000 Corval Hill Pty Ltd,&nbsp; Ph (1300) 555 014,&nbsp; Fax (1300) 555 027</div>
  </div>
</section>

<section class="page page--detail">
  <div class="abs detail-ref">referrer name</div>
  <table class="abs ledger">
    <colgroup><col class="c1"><col class="c2"><col class="c3"><col class="c4"><col class="c5"><col class="c6"><col class="c7"><col class="c8"></colgroup>
    <thead><tr><th>Client</th><th>Lender</th><th>Loan Amount</th><th>Upfront</th><th>Trail</th><th>Adj.</th><th>GST</th><th>TOTAL</th></tr></thead>
    <tbody>
      <tr><td>dsgfg</td><td>Kestrel Bank</td><td>$34,182.00</td><td>$0.00</td><td>$3.48</td><td>$0.00</td><td>$0.35</td><td>$3.83</td></tr>
      <tr><td>ggffgfd</td><td>Kestrel Bank</td><td>$132,583.00</td><td>$0.00</td><td>$13.51</td><td>$0.00</td><td>$1.35</td><td>$14.86</td></tr>
      <tr><td>fggfdfg</td><td>Kestrel Bank</td><td>$119,988.00</td><td>$0.00</td><td>$12.23</td><td>$0.00</td><td>$1.22</td><td>$13.45</td></tr>
      <tr><td>gfdfg</td><td>Kestrel Bank</td><td>$479,999.00</td><td>$0.00</td><td>$48.92</td><td>$0.00</td><td>$4.89</td><td>$53.81</td></tr>
      <tr><td>dfg</td><td>Kestrel Bank</td><td>$134,161.00</td><td>$0.00</td><td>$13.67</td><td>$0.00</td><td>$1.37</td><td>$15.04</td></tr>
      <tr><td>gdfg</td><td>Kestrel Bank</td><td>$78,927.00</td><td>$0.00</td><td>$8.05</td><td>$0.00</td><td>$0.81</td><td>$8.86</td></tr>
      <tr><td>dffdgvfgf</td><td>Kestrel Bank</td><td>$149,400.00</td><td>$0.00</td><td>$15.22</td><td>$0.00</td><td>$1.52</td><td>$16.74</td></tr>
      <tr><td>fgdg</td><td>Kestrel Bank</td><td>$99,805.00</td><td>$0.00</td><td>$10.17</td><td>$0.00</td><td>$1.02</td><td>$11.19</td></tr>
      <tr><td>ffgdggf</td><td>Kestrel Bank</td><td>$377,100.00</td><td>$0.00</td><td>$38.43</td><td>$0.00</td><td>$3.84</td><td>$42.27</td></tr>
      <tr><td>df</td><td>Kestrel Bank</td><td>$101,738.00</td><td>$0.00</td><td>$10.37</td><td>$0.00</td><td>$1.04</td><td>$11.41</td></tr>
      <tr><td>gdgsdgsdf</td><td>Kestrel Bank</td><td>$50,564.00</td><td>$0.00</td><td>$5.15</td><td>$0.00</td><td>$0.52</td><td>$5.67</td></tr>
      <tr><td>dsfggddfg</td><td>Kestrel Bank</td><td>$108,500.00</td><td>$0.00</td><td>$7.38</td><td>$0.00</td><td>$0.74</td><td>$8.12</td></tr>
      <tr><td>dfdfgdsfghfd</td><td>Kestrel Bank</td><td>$230,807.00</td><td>$0.00</td><td>$15.68</td><td>$0.00</td><td>$1.57</td><td>$17.25</td></tr>
      <tr><td>dfdjsf</td><td>Southline Bank</td><td>$600,000.00</td><td>$3,000.00</td><td>$0.00</td><td>$0.00</td><td>$300.00</td><td>$3,300.00</td></tr>
    </tbody>
  </table>
  <div class="abs rule-notes">
    <div class="row"><span class="label">- only applies in months with a new settlement occurring</span><span class="v neg" style="width:86px;margin-left:86px">-$50.00</span><span class="v neg" style="width:74px">-$5.00</span><span class="v neg" style="width:123px">-$55.00</span></div>
    <div class="row"><span class="label">deducted from trail if <u>no new deals within last 6 months</u></span><span class="v" style="width:86px;margin-left:86px">$0.00</span><span class="v" style="width:74px">$0.00</span><span class="v" style="width:123px">$0.00</span></div>
  </div>
  <table class="abs summary">
    <colgroup><col style="width:198px"><col style="width:110px"><col style="width:86px"><col style="width:86px"><col style="width:66px"><col style="width:74px"><col style="width:123px"></colgroup>
    <thead><tr><th style="background:none"></th><th>Loan Book</th><th>Upfront</th><th>Trail</th><th>Adj.</th><th>GST</th><th>TOTAL</th></tr></thead>
    <tbody><tr><td></td><td>$2,697,754.00</td><td>$3,000.00</td><td>$202.26</td><td class="neg">-$50.00</td><td>$315.24</td><td class="boxed"><span>$3,467.50</span></td></tr></tbody>
  </table>
</section>

</body>
</html>
```